Spread for a luxury home magazine

- introduce owner and team with headshots and bios
- list benefits of choosing our title company
- luxury/elegant aesthetic

Will send more headshots and bios as things progress

```html
<!DOCTYPE html>
<html lang="en">
<head>
<meta charset="UTF-8">
<title>Heritage Crest Title – Meet the Team Spread</title>
<link href="https://fonts.googleapis.com/css2?family=Cinzel:wght@400;500&family=Cormorant+Garamond:wght@400;500&family=Great+Vibes&family=Oswald:wght@400;600&family=Poppins:wght@300;400&display=swap" rel="stylesheet">
<style>
  :root {
    --page-bg: #dfe6ee;
    --ink-black: #1b1a1a;
    --panel-black: #161515;
    --gold: #b08f36;
    --gold-light: #c9a74a;
    --gold-deep: #6f5815;
    --gold-col: #86691c;
    --text-light: #ece6d8;
    --text-dim: #cfc8b8;
    --rule: #6d6a63;
  }
  * { margin: 0; padding: 0; box-sizing: border-box; }
  html, body { width: 807px; height: 1200px; overflow: hidden; }
  body { background: var(--page-bg); font-family: "Poppins", sans-serif; position: relative; }

  .spread {
    position: absolute; left: 0; top: 363px;
    width: 807px; height: 474px;
    background: var(--ink-black);
    box-shadow: 0 6px 18px rgba(0,0,0,.25);
    overflow: hidden;
  }

  /* ---------- Cover panel ---------- */
  .cover { position: absolute; left: 0; top: 0; width: 247px; height: 474px; background: var(--panel-black); }
  .brand { position: absolute; left: 0; width: 247px; top: 44px; text-align: center; }
  .brand-mark { display: block; width: 22px; height: 22px; margin: 0 auto 9px; border: 1.5px solid var(--gold); }
  .brand-name { font-family: "Cinzel", serif; font-size: 13px; color: var(--text-light); letter-spacing: .5px; }

  .tagline { position: absolute; left: 25px; top: 116px; }
  .tagline-script { font-family: "Great Vibes", cursive; font-size: 27px; color: var(--gold); line-height: 1; word-spacing: 4px; }
  .tagline-main { font-family: "Cormorant Garamond", serif; font-size: 24px; color: var(--text-light); line-height: 22px; letter-spacing: .5px; }
  .gold-rule { position: absolute; left: 29px; top: 210px; width: 52px; height: 1.5px; background: var(--gold); }

  .services { position: absolute; left: 12px; top: 222px; width: 225px; display: flex; }
  .service { flex: 1; text-align: center; border-right: 1px dashed var(--rule); }
  .service:last-child { border-right: none; }
  .service svg { width: 26px; height: 26px; display: block; margin: 0 auto 3px; }
  .service span { font-size: 5px; color: var(--text-light); line-height: 6px; display: block; }

  .house-photo { position: absolute; left: 0; top: 274px; width: 247px; height: 135px; background: linear-gradient(160deg, #8a8068 0%, #5b5540 45%, #3e5a2c 80%, #4f7336 100%); }
  .house-frame { position: absolute; left: 14px; top: 286px; width: 221px; height: 111px; border: 1px solid rgba(255,255,255,.55); }
  .site-url { position: absolute; left: 31px; top: 434px; font-size: 8.5px; letter-spacing: 1.4px; color: var(--text-light); }

  /* ---------- Owner column ---------- */
  .owner { position: absolute; left: 247px; top: 0; width: 134px; height: 474px; background: linear-gradient(180deg, var(--gold-col) 0%, #7b6119 60%, var(--gold-deep) 100%); text-align: center; color: var(--text-light); }
  .owner-script { font-family: "Great Vibes", cursive; font-size: 25px; line-height: 1; padding-top: 24px; }
  .owner-title { font-family: "Cormorant Garamond", serif; font-size: 18px; line-height: 1; letter-spacing: .5px; }
  .owner-rule { width: 56px; height: 1px; background: var(--text-light); margin: 8px auto 10px; }
  .owner-name { font-family: "Oswald", sans-serif; font-weight: 600; font-size: 12px; color: #e2c36a; line-height: 1.1; }
  .owner-role { font-size: 7px; margin-bottom: 6px; }
  .owner-bio { font-size: 5.6px; line-height: 7.4px; padding: 0 8px; }
  .owner-photo { position: absolute; left: -14px; top: 223px; width: 148px; height: 251px; background: radial-gradient(ellipse at 50% 25%, #6e5a3f 0%, #3a2e22 45%, #1d1a17 80%); border-radius: 60px 60px 0 0; }

  /* ---------- Team page ---------- */
  .team { position: absolute; left: 381px; top: 0; width: 426px; height: 474px; background: linear-gradient(170deg, #22201e 0%, #1a1918 50%, #201f1d 100%); }
  .team-heading { position: absolute; left: 44px; top: 20px; display: flex; align-items: baseline; }
  .team-heading .script { font-family: "Great Vibes", cursive; font-size: 26px; color: var(--gold); line-height: 1; }
  .team-heading .caps { font-family: "Cormorant Garamond", serif; font-size: 18px; color: var(--text-light); letter-spacing: .5px; margin-left: 1px; }

  .member { position: absolute; left: 44px; width: 284px; }
  .member-name { font-family: "Oswald", sans-serif; font-size: 7px; font-weight: 600; color: var(--gold-light); letter-spacing: .2px; margin-bottom: 2px; }
  .member-name .last { font-weight: 400; }
  .member p { font-size: 3.3px; line-height: 4.3px; color: var(--text-dim); margin-bottom: 3px; }
  .member-divider { position: absolute; left: 44px; width: 284px; border-top: 0.7px dashed var(--rule); }

  .headshot { position: absolute; left: 342px; width: 48px; height: 48px; background: radial-gradient(circle at 50% 40%, #8b6f58 0%, #4c3a2e 55%, #2a2420 100%); }
  .headshot::after { content: ""; position: absolute; left: 3px; top: -3px; right: -3px; bottom: 3px; border: 0.8px solid var(--gold); }
</style>
</head>
<body>
  <section class="spread">
    <div class="cover">
      <div class="brand">
        <span class="brand-mark"></span>
        <div class="brand-name">Heritage Crest Title</div>
      </div>
      <div class="tagline">
        <div class="tagline-script">Your Premier</div>
        <div class="tagline-main">SOUTH TEXAS<br>TITLE COMPANY</div>
      </div>
      <div class="gold-rule"></div>
      <div class="services">
        <div class="service">
          <svg viewBox="0 0 26 26" fill="none" stroke="#b08f36" stroke-width="1.2"><rect x="6" y="3" width="13" height="19"/><line x1="9" y1="8" x2="16" y2="8"/><line x1="9" y1="11" x2="16" y2="11"/><line x1="9" y1="14" x2="14" y2="14"/><path d="M14 21 l6 -8 l2 2 l-6 8 z"/></svg>
          <span>Property<br>Title Services</span>
        </div>
        <div class="service">
          <svg viewBox="0 0 26 26" fill="none" stroke="#b08f36" stroke-width="1.2"><path d="M4 12 L13 4 L22 12"/><path d="M7 10 V22 H19 V10"/><path d="M9 17 l3 -2 l2 2 l3 -2"/></svg>
          <span>Realtor<br>Title Services</span>
        </div>
        <div class="service">
          <svg viewBox="0 0 26 26" fill="none" stroke="#b08f36" stroke-width="1.2"><rect x="11" y="3" width="12" height="9"/><line x1="13" y1="9" x2="16" y2="6"/><line x1="16" y1="6" x2="21" y2="8"/><circle cx="7" cy="7" r="2.2"/><path d="M4 22 V12 h6 V22"/><line x1="4" y1="22" x2="23" y2="22"/></svg>
          <span>Coaching<br>Services</span>
        </div>
      </div>
      <div class="house-photo" role="img" aria-label="Photograph of a luxury stone home with arched entry and landscaped lawn"></div>
      <div class="house-frame"></div>
      <div class="site-url">www.heritagecresttitle.com</div>
    </div>

    <div class="owner">
      <div class="owner-script">Meet</div>
      <div class="owner-title">THE OWNER</div>
      <div class="owner-rule"></div>
      <div class="owner-name">ELENA R. MARQUEZ</div>
      <div class="owner-role">Founder &amp; Owner</div>
      <p class="owner-bio">Growing up in San Antonio, TX, Elena R. Marquez always knew she would work with people as building relationships always came naturally to her. This inherent interest in others led to her studies at Lone Star University where she earned a Bachelor of Science in Human Development and Family Studies.</p>
      <div class="owner-photo" role="img" aria-label="Portrait photograph of the founder and owner"></div>
    </div>

    <div class="team">
      <div class="team-heading"><span class="script">Meet</span><span class="caps">THE TEAM</span></div>

      <div class="member" style="top:56px">
        <div class="member-name">SIENNA <span class="last">CALDWELL</span></div>
        <p>With a background in hospitality and a love for organized details, I joined the escrow team ready to make every transaction feel simple. As an Escrow Assistant I prepare files, track deadlines and keep buyers, sellers and agents informed from the opening of escrow to the final signature, so each closing day feels calm and well prepared.</p>
        <p>Away from the desk I enjoy long walks, live music and trying new restaurants around town with friends and family.</p>
      </div>
      <div class="member-divider" style="top:108px"></div>
      <div class="headshot" style="top:51px" role="img" aria-label="Headshot of Sienna Caldwell"></div>

      <div class="member" style="top:117px">
        <div class="member-name">NOELLE <span class="last">BRANDT</span></div>
        <p>I came to title work from a career in client service, and I love building lasting partnerships with agents and lenders. Every file is a chance to solve problems early, communicate clearly and deliver a smooth, on-time closing for everyone involved.</p>
        <p>In my free time I enjoy gardening, reading mystery novels and planning weekend road trips across the state.</p>
      </div>
      <div class="member-divider" style="top:168px"></div>
      <div class="headshot" style="top:113px" role="img" aria-label="Headshot of Noelle Brandt"></div>

      <div class="member" style="top:177px">
        <div class="member-name">VIVIAN <span class="last">TORRES</span></div>
        <p>After years in real estate administration and transaction coordination, I found my home at the closing table. I have handled residential, commercial and land transactions, and I bring patience, precision and a warm welcome to every client who walks through our door. Buying a home is a milestone worth celebrating.</p>
        <p>When I am not in the office you will find me painting, volunteering at local events or relaxing at home with a good cup of coffee and a classic movie.</p>
      </div>
      <div class="member-divider" style="top:240px"></div>
      <div class="headshot" style="top:180px" role="img" aria-label="Headshot of Vivian Torres"></div>

      <div class="member" style="top:253px">
        <div class="member-name">DANA <span class="last">WHITMORE</span></div>
        <p>An upbeat closer who works with agents of every experience level, I keep the process organized from accepted offer to final walkthrough. Clients leave our office confident, informed and excited to begin the next chapter in their new home.</p>
      </div>
      <div class="member-divider" style="top:305px"></div>
      <div class="headshot" style="top:245px" role="img" aria-label="Headshot of Dana Whitmore"></div>

      <div class="member" style="top:313px">
        <div class="member-name">ROSA <span class="last">DELGADO</span></div>
        <p>I believe great service starts with kindness and careful listening. I treat every file as if it were my own family's purchase, and I pay close attention to every detail so our partners can count on a smooth, accurate closing every time.</p>
      </div>
      <div class="member-divider" style="top:363px"></div>
      <div class="headshot" style="top:305px" role="img" aria-label="Headshot of Rosa Delgado"></div>

      <div class="member" style="top:372px">
        <div class="member-name">MARCUS <span class="last">ELLERY</span></div>
        <p>Before joining the title industry I spent several years in operations and project management, where I learned how strong teams stay calm and focused under pressure. I bring that same steady approach to every closing.</p>
        <p>I know firsthand how stressful buying a home can feel, which is why my goal is simple: every client deserves a clear, friendly and well organized closing experience, regardless of price point.</p>
        <p>For fun I enjoy cooking for friends, cycling on weekend mornings and cheering on my favorite teams.</p>
      </div>
      <div class="headshot" style="top:374px" role="img" aria-label="Headshot of Marcus Ellery"></div>
    </div>
  </section>
</body>
</html>
```